We need a web designer/programmer for Bright Ferns Ltd in London who's primary aid is to assist young people to find activities they'd like to do in their area. the PursuitFinder is mainly a post code or key word search engine. my brief attached shows what I want the web to do and how it should look. the Friends/VyTrers page is almost like a dating site. instead of choose blond hair blue eyed, young people search for friend who's doing similar activities or wearing the same size mountain boot etc so that they could share. hope it all make sense. I really want the website to go live and launch party at the end of Sept/early Oct. hope that's realistic. Thank you. Regards, Wen

Target Market(s)

young people 14-25

Number of Pages Required

5+ page

Font styles to use
Sans Serif

Requirements
Must have
• search engine, interactive, chat, user registration. remote editing with security code for my customers.
• needs to be colourful to attract young people.
• colour match the Bright Ferns Logo
Nice to have
• matching style to the VyTr-hub.org web

```html
<!DOCTYPE html>
<html lang="en">
<head>
<meta charset="utf-8">
<title>Bright Ferns</title>
<link href="https://fonts.googleapis.com/css2?family=Quicksand:wght@500;600;700&display=swap" rel="stylesheet">
<style>
  :root{
    --page:#ffffff;
    --ink:#3a3a3a;
    --ink-soft:#555;
    --green:#5a9a10;
    --maroon:#8d1535;
    --orange:#ff8c00;
    --plum:#4b0a1f;
    --pink:#e0185a;
    --sticker:#d81b5c;
    --tile-green:#5c9a12;
    --tile-wine:#62202c;
    --tile-gold:#ffb20a;
    --tile-forest:#2f8a14;
    --gold-text:#ffd21a;
    --panel:#f1f1f1;
    --line:#dcdcdc;
    --footer:#ededed;
  }
  *{box-sizing:border-box;margin:0;padding:0}
  html,body{width:1009px;height:1200px;overflow:hidden;background:var(--page)}
  body{font-family:"Quicksand",sans-serif;color:var(--ink);position:relative}
  .abs{position:absolute}

  .brand{left:62px;top:6px;width:108px;height:94px;display:flex;align-items:center;justify-content:center;gap:6px;font-weight:700;font-size:15px;color:var(--green)}
  .brand-dot{width:14px;height:14px;border-radius:50%;background:var(--pink)}

  .main-nav{left:270px;top:58px;display:flex;gap:3px}
  .main-nav a{display:flex;align-items:center;justify-content:center;height:38px;color:#fff;text-decoration:none;font-size:12px;font-weight:600;letter-spacing:.3px}
  .nav-rule{left:266px;top:96px;width:681px;height:3px;background:var(--line)}

  .contact-title{left:744px;top:20px;font-size:15px;color:var(--ink-soft)}
  .social{left:744px;top:53px;display:flex;gap:8px}
  .social span{width:35px;height:35px;border-radius:50%;background:#eef0f4;border:2px solid #c8ccd4;display:flex;align-items:center;justify-content:center}

  .slider{left:62px;top:107px;width:658px;height:335px;background:#ddd;padding:4px}
  .slide-photo{width:100%;height:100%;background:linear-gradient(160deg,#dfe7ee 0%,#c7b9a8 40%,#7ab7b5 70%,#e9ecef 100%);position:relative}
  .arrow{position:absolute;top:134px;width:26px;height:26px;border-radius:50%;background:#333;display:flex;align-items:center;justify-content:center}
  .caption{position:absolute;left:0;right:0;bottom:0;height:84px;background:rgba(40,40,40,.82);padding:8px 20px}
  .caption h2{color:var(--gold-text);font-size:22px;font-weight:600;line-height:26px}
  .caption p{color:#fff;font-size:13.5px;line-height:20px;font-weight:500}

  .welcome{left:62px;top:464px;width:660px}
  .welcome h1{font-size:20px;font-weight:600;margin-bottom:8px}
  .welcome p{font-size:10.5px;line-height:18px;color:var(--ink-soft);font-weight:500}

  .tile{width:315px;height:239px;padding:10px 13px}
  .tile h3{color:#fff;font-size:21px;font-weight:600;line-height:26px;margin-bottom:8px}
  .tile-photo{width:290px;height:179px}

  .sidebar{left:744px;top:107px;width:203px;height:542px;background:var(--panel);border:1px solid var(--line)}
  .sticker{width:80px;height:73px;background:var(--sticker);color:#fff;font-size:13.5px;font-weight:600;line-height:16px;display:flex;align-items:center;justify-content:center;text-align:center}

  .site-footer{left:0;top:1111px;width:1009px;height:89px;background:var(--footer);text-align:center}
  .footer-nav{display:flex;justify-content:center;gap:24px;margin-top:24px;font-size:10px;font-weight:600;color:var(--ink-soft)}
  .copyright{margin-top:10px;font-size:9.5px;line-height:16px;color:#777}
</style>
</head>
<body>

<div class="abs brand"><span class="brand-dot"></span>Bright Ferns</div>

<nav class="abs main-nav">
  <a style="width:72px;background:var(--green)">HOME</a>
  <a style="width:116px;background:var(--maroon)">AAP LISTING</a>
  <a style="width:83px;background:var(--orange)">VYTRER</a>
  <a style="width:83px;background:var(--plum)">GALLERY</a>
  <a style="width:83px;background:var(--pink)">APP</a>
</nav>
<div class="abs nav-rule"></div>

<div class="abs contact-title">Contact Us &amp; Follow Us</div>
<div class="abs social">
  <span aria-label="Social link"></span>
  <span aria-label="Social link"></span>
  <span aria-label="Email"><svg width="16" height="12" viewBox="0 0 16 12"><rect x="0.5" y="0.5" width="15" height="11" rx="1.5" fill="#fff" stroke="#4a5a8a"/><path d="M1 1l7 6 7-6" fill="none" stroke="#4a5a8a"/></svg></span>
  <span aria-label="Social link"></span>
  <span aria-label="Phone"><svg width="16" height="16" viewBox="0 0 16 16"><path d="M4 1l3 3-2 2c1 2 3 4 5 5l2-2 3 3-2 3C7 15 1 9 1 3z" fill="#666"/></svg></span>
</div>

<section class="abs slider">
  <div class="slide-photo" role="img" aria-label="Photo of young friends laughing outdoors in bright daylight">
    <span class="arrow" style="left:10px"><svg width="10" height="10" viewBox="0 0 10 10"><path d="M7 1L3 5l4 4" fill="none" stroke="#fff" stroke-width="2"/></svg></span>
    <span class="arrow" style="right:10px"><svg width="10" height="10" viewBox="0 0 10 10"><path d="M3 1l4 4-4 4" fill="none" stroke="#fff" stroke-width="2"/></svg></span>
    <div class="caption">
      <h2>What We Do</h2>
      <p>Aliquam molestie, mi et imperdiet euismod, dui purus auctor tellus, et interdum lacus lectus et ante. Sed accumsan sollicitudin sapien, sit amet adipiscing turpis gravida ac.</p>
    </div>
  </div>
</section>

<section class="abs welcome">
  <h1>Welcome to Bright Ferns</h1>
  <p>Aliquam molestie, mi et imperdiet euismod, dui purus auctor tellus, et interdum lacus lectus et ante. Sed accumsan sollicitudin sapien, sit amet adipiscing turpis gravida ac. In congue, neque ac lobortis volutpat, libero mauris varius mi, vitae suscipit ipsum ligula vitae risus. Duis aliquam nibh a dui iaculis viverra id a velit. Vivamus egestas risus in magna varius commodo. Sed semper viverra egestas. Etiam pretium porttitor lectus, vel ornare neque porta volutpat.</p>
</section>

<article class="abs tile" style="left:62px;top:593px;background:var(--tile-green)">
  <h3>AAP listing@BrightFerns</h3>
  <div class="tile-photo" role="img" aria-label="Photo of a smiling team gathered around a desk in an office" style="background:linear-gradient(135deg,#e6e6e2,#9a8e7c 55%,#4a4a48)"></div>
</article>
<article class="abs tile" style="left:405px;top:593px;background:var(--tile-wine)">
  <h3>AAP listing@BrightFerns</h3>
  <div class="tile-photo" role="img" aria-label="Photo of young friends cheering by a tent at a campsite" style="background:linear-gradient(135deg,#3d5f8a,#7d9a55 50%,#c9a98a)"></div>
</article>
<article class="abs tile" style="left:62px;top:849px;background:var(--tile-gold)">
  <h3>Gallery@BrightFerns</h3>
  <div class="tile-photo" role="img" aria-label="Photo of a happy group of teenagers posing together outdoors" style="background:linear-gradient(135deg,#4f7a3a,#d9b59a 50%,#f2eee8)"></div>
</article>
<article class="abs tile" style="left:405px;top:849px;background:var(--tile-forest)">
  <h3>AAP@BrightFerns</h3>
  <div class="tile-photo" role="img" aria-label="Photo of an elephant and calf on savanna grassland" style="background:linear-gradient(180deg,#8fc0e4,#b9cfe0 45%,#7d7060 75%,#9c8a6a)"></div>
</article>

<aside class="abs sidebar">
  <div class="abs sticker" style="left:13px;top:14px">Advertise<br>Sticker</div>
  <div class="abs sticker" style="left:107px;top:14px">Advertise<br>Sticker</div>
  <div class="abs sticker" style="left:13px;top:102px">Advertise<br>Sticker</div>
  <div class="abs sticker" style="left:107px;top:102px">Advertise<br>Sticker</div>
  <div class="abs sticker" style="left:13px;top:189px">Advertise<br>Sticker</div>
  <div class="abs sticker" style="left:107px;top:189px">Advertise<br>Sticker</div>
  <div class="abs sticker" style="left:13px;top:277px">Advertise<br>Sticker</div>
  <div class="abs sticker" style="left:107px;top:277px">Advertise<br>Sticker</div>
  <div class="abs sticker" style="left:13px;top:364px">Advertise<br>Sticker</div>
  <div class="abs sticker" style="left:107px;top:364px">Advertise<br>Sticker</div>
  <div class="abs sticker" style="left:13px;top:452px">Advertise<br>Sticker</div>
  <div class="abs sticker" style="left:107px;top:452px">Advertise<br>Sticker</div>
</aside>

<footer class="abs site-footer">
  <nav class="footer-nav"><span>HOME</span><span>AAP LISTING</span><span>VYTRER</span><span>GALLERY</span><span>APP</span></nav>
  <p class="copyright">Copyright © 2014. Company Name.<br>All Right Reserved</p>
</footer>

</body>
</html>
```